VELOQUARD Stationery Design Project

I want a stationery design for a web development company consists of:
1- business card
2- Letter Head
3- small Envelope
4- Large Envelope

need a very clean professional simple design yet creative,

The company logo is attached
http://www.artpitchly.com/project-progress/designs.aspx?briefId=5173048&submissionId=73920416

logo font is sui generis rg (attached)
I would like to have the stationery text font to be helvetica font regular or light (can be changed)

I love the combination of cyan, black and grey colors
( will attach some recommended styles)

Industry/Entity Type

Business

Requirements
Should not have
• curves or waves

```html
<!DOCTYPE html>
<html lang="en">
<head>
<meta charset="utf-8">
<title>VELOQUARD Stationery</title>
<link href="https://fonts.googleapis.com/css2?family=Arimo:wght@400;700&display=swap" rel="stylesheet">
<style>
  :root {
    --bg: #c9c8cb;
    --paper: #f4f4f4;
    --dark: #313131;
    --dark-edge: #2a2a2a;
    --cyan: #3a9ad9;
    --grey: #9a9a9a;
    --text-grey: #7d7d7d;
  }
  * { margin: 0; padding: 0; box-sizing: border-box; }
  html, body { width: 1200px; height: 991px; overflow: hidden; }
  body {
    background: var(--bg);
    font-family: "Arimo", Helvetica, Arial, sans-serif;
    position: relative;
  }
  .piece { position: absolute; box-shadow: 0 1px 3px rgba(0,0,0,.25); overflow: hidden; }
  .paper { background: var(--paper); }
  .dark { background: var(--dark); }

  .stripe { position: absolute; left: 0; right: 0; bottom: 0; height: 4px; background: var(--grey); }
  .stripe::after {
    content: ""; position: absolute; right: 0; top: 0; bottom: 0; width: 30%;
    background: var(--cyan);
    clip-path: polygon(4px 0, 100% 0, 100% 100%, 0 100%);
  }

  .brand { position: absolute; display: flex; align-items: center; gap: 6px; }
  .brand-mark { background: var(--cyan); }
  .brand-name { color: var(--cyan); font-weight: 400; letter-spacing: .04em; }

  .contact { position: absolute; font-size: 5px; line-height: 7px; color: var(--text-grey); }
  .contact li { list-style: none; display: flex; align-items: center; gap: 3px; }
  .contact .ico { width: 5px; height: 5px; background: var(--cyan); border-radius: 1px; }
  .contact .addr { margin-top: 3px; }

  /* Letterhead */
  .letterhead { left: 71px; top: 104px; width: 398px; height: 560px; }
  .letterhead .brand { left: 34px; top: 48px; }
  .letterhead .brand-mark { width: 12px; height: 12px; }
  .letterhead .brand-name { font-size: 14px; }
  .letterhead .contact { left: 298px; top: 30px; }

  /* Folder */
  .folder { left: 507px; top: 90px; width: 432px; height: 576px; border-radius: 3px 3px 0 0; }
  .folder .spine { position: absolute; left: 27px; top: 0; bottom: 0; width: 1px; background: var(--dark-edge); }
  .folder .brand { left: 0; right: 0; top: 128px; justify-content: center; }
  .folder .brand-mark { width: 16px; height: 16px; }
  .folder .brand-name { font-size: 21px; }

  /* Business cards */
  .card { width: 170px; height: 94px; }
  .card-front { left: 66px; top: 696px; }
  .card-front .brand { left: 22px; top: 40px; }
  .card-front .brand-mark { width: 6px; height: 6px; }
  .card-front .brand-name { font-size: 9px; }
  .card-front .divider { position: absolute; left: 89px; top: 18px; width: 1px; height: 56px; background: #dcdcdc; }
  .card-front .holder { position: absolute; left: 99px; top: 22px; }
  .card-front .holder-name { font-size: 5px; font-weight: 700; color: var(--cyan); }
  .card-front .holder-role { font-size: 4px; color: var(--text-grey); }
  .card-front .contact { left: 99px; top: 36px; font-size: 4px; line-height: 5.2px; }
  .card-front .contact .ico { width: 4px; height: 4px; }
  .card-back { left: 66px; top: 810px; }
  .card-back .brand { left: 0; right: 0; top: 40px; justify-content: center; }
  .card-back .brand-mark { width: 7px; height: 7px; }
  .card-back .brand-name { font-size: 10px; }

  /* Large envelope */
  .envelope-large { left: 266px; top: 696px; width: 415px; height: 208px; }
  .envelope-large .brand { left: 22px; top: 46px; }
  .envelope-large .brand-mark { width: 10px; height: 10px; }
  .envelope-large .brand-name { font-size: 13px; }
  .envelope-large .return-address {
    position: absolute; left: 22px; top: 176px; padding-left: 5px;
    border-left: 1px solid var(--cyan);
    font-size: 5px; line-height: 6.5px; color: #a5a5a5;
  }

  /* Small envelope */
  .envelope-small { left: 718px; top: 696px; width: 415px; height: 208px; }
  .envelope-small .flap { position: absolute; left: 0; top: 0; }
  .envelope-small .flap-mark {
    position: absolute; left: 197px; top: 20px; width: 16px; height: 16px; background: var(--cyan);
  }
  .envelope-small .web {
    position: absolute; left: 0; right: 0; top: 180px; text-align: center;
    font-size: 5px; color: #555;
  }
  .envelope-small .web span { color: var(--cyan); }
</style>
</head>
<body>

<section class="piece paper letterhead" aria-label="Letterhead">
  <div class="brand"><span class="brand-mark"></span><span class="brand-name">VELOQUARD</span></div>
  <ul class="contact">
    <li><span class="ico"></span>555-014-2280</li>
    <li><span class="ico"></span>555-014-2291</li>
    <li><span class="ico"></span>www.veloquard.com</li>
    <li class="addr">4820 Larkfield Ave, Suite 310</li>
    <li>Austin, TX 78701</li>
  </ul>
  <div class="stripe"></div>
</section>

<section class="piece dark folder" aria-label="Presentation folder">
  <div class="spine"></div>
  <div class="brand"><span class="brand-mark"></span><span class="brand-name">VELOQUARD</span></div>
  <div class="stripe"></div>
</section>

<section class="piece paper card card-front" aria-label="Business card front">
  <div class="brand"><span class="brand-mark"></span><span class="brand-name">VELOQUARD</span></div>
  <div class="divider"></div>
  <div class="holder">
    <div class="holder-name">MARA ELLISON</div>
    <div class="holder-role">General Manager</div>
  </div>
  <ul class="contact">
    <li><span class="ico"></span>555-014-2280</li>
    <li><span class="ico"></span>555-014-2291</li>
    <li><span class="ico"></span>info@veloquard.com</li>
    <li><span class="ico"></span>www.veloquard.com</li>
    <li class="addr">4820 Larkfield Ave, Suite 310</li>
    <li>Austin, TX 78701</li>
  </ul>
  <div class="stripe"></div>
</section>

<section class="piece dark card card-back" aria-label="Business card back">
  <div class="brand"><span class="brand-mark"></span><span class="brand-name">VELOQUARD</span></div>
</section>

<section class="piece dark envelope-large" aria-label="Large envelope">
  <div class="brand"><span class="brand-mark"></span><span class="brand-name">VELOQUARD</span></div>
  <div class="return-address">4820 Larkfield Ave, Suite 310<br>Austin, TX 78701</div>
  <div class="stripe"></div>
</section>

<section class="piece paper envelope-small" aria-label="Small envelope">
  <svg class="flap" width="415" height="60" viewBox="0 0 415 60" aria-hidden="true">
    <polygon points="0,0 415,0 400,50 395,58 20,58 15,50" fill="var(--dark)"/>
  </svg>
  <span class="flap-mark"></span>
  <div class="web">www.<span>veloquard</span>.com</div>
</section>

</body>
</html>
```